Commercial janitorial cleaning

Janitorial cleaning particularly for commercial buildings. Website needs to specify free estimates. Location of service is Millbrook, Ashford, Easton Falls, Cedarvale, Harlow ny area. Services page with Janitorial services- General Office Cleaning, Construction Cleaning, Carpet Extraction, Consultation/Business, Lighting Maintenance, Seasonal Deep Cleaning, Window cleaning, Event Cleaning, Floor and Carpet Cleaning, Floor Striping and Waxing. Contact us page with email phone number on page and a request page that emails me if they have any questions. About us page-the picture of my family on it with a section I can type a story myself.

Target Market(s)

Commercial businesses

Industry/Entity Type

Janitorial Service

Number of Pages Required

4 page

Font styles to use
Serif
Sans Serif
Script

Colors
ec1f27
1b1b1b
ffffff
9d9d9d

Requirements
Must have
• Phone number 555-314-2760. Must have free estimates on home page. Going for industrial / modern look to website
Nice to have
• Logo is a red and black building so if those colors could be coordinated to website that would be awesome.

```html
<!DOCTYPE html>
<html lang="en">
<head>
<meta charset="utf-8">
<title>Tidewell Cleaning Services</title>
<link href="https://fonts.googleapis.com/css2?family=Questrial&family=Roboto:ital,wght@0,400;0,500;0,700;1,400&display=swap" rel="stylesheet">
<style>
:root{
  --red:#ec1f27;
  --ink:#1b1b1b;
  --white:#ffffff;
  --grey:#9d9d9d;
  --text:#555555;
  --line:#dddddd;
  --light:#eeeeee;
}
*{box-sizing:border-box;margin:0;padding:0}
html,body{width:1200px;height:3593px;overflow:hidden}
body{position:relative;background:var(--white);font-family:"Roboto",Arial,sans-serif;color:var(--text)}
.abs{position:absolute}
h2{font-family:"Questrial",Arial,sans-serif;font-weight:400;color:var(--ink);text-align:center;font-size:38px}
.title-rule{width:96px;height:2px;background:var(--red);margin:0 auto 14px}

/* top bar */
.topbar{left:0;top:0;width:1200px;height:31px;background:var(--ink);color:var(--white);font-size:13px}
.topbar .social{left:79px;top:9px;display:flex;gap:6px}
.topbar .social span{width:12px;height:12px;background:var(--white);border-radius:2px}
.topbar .contact{right:79px;top:7px;display:flex;gap:26px}
.topbar svg{vertical-align:-2px;margin-right:6px}

/* header */
.header{left:0;top:31px;width:1200px;height:77px;background:var(--white);box-shadow:0 1px 3px rgba(0,0,0,.08)}
.brand{left:79px;top:14px;display:flex;align-items:center;gap:12px}
.brand .mark{width:36px;height:36px;background:var(--red)}
.brand .name{font-weight:700;font-size:19px;line-height:23px;color:var(--ink)}
.nav{left:514px;top:30px;display:flex;gap:26px;font-size:15px;color:#666}
.free-quote{left:1030px;top:0;width:80px;height:69px;background:var(--red);color:var(--white);font-weight:700;font-size:17px;line-height:19px;text-align:center;padding-top:15px}

/* hero */
.hero{left:0;top:108px;width:1200px;height:490px}
.hero .photo{position:absolute;inset:0;background:linear-gradient(100deg,#9aa0a8 0%,#c9ccd0 35%,#6d7683 60%,#3d4a5e 100%)}
.hero .curve{position:absolute;left:0;bottom:0}
.hero h1{left:79px;top:122px;font-family:"Questrial",Arial,sans-serif;font-weight:400;font-size:38px;color:var(--white);letter-spacing:1px}
.hero p{left:79px;top:190px;width:560px;font-size:14px;line-height:21px;color:var(--white)}
.hero .btn{left:79px;top:275px;width:177px;height:38px;border:1px solid var(--white);color:var(--white);font-weight:700;font-size:15px;letter-spacing:1px;text-align:center;line-height:36px}

/* quality */
.quality{left:0;top:642px;width:1200px}
.quality .lead{width:960px;margin:0 auto;text-align:center;font-size:13px;line-height:20px}
.team-photo{left:108px;top:802px;width:520px;height:324px;background:radial-gradient(ellipse at center,#6aa8d8 0%,#c8dcea 55%,#ffffff 80%)}
.feature{left:742px;width:380px;display:flex;gap:20px}
.feature .icon{width:72px;height:72px;border-radius:50%;background:var(--red);flex:none;display:flex;align-items:center;justify-content:center}
.feature h3{font-size:14px;font-weight:500;color:var(--ink);margin:6px 0 10px}
.feature p{font-size:13px;line-height:21px;width:230px}

/* services */
.services{left:0;top:1190px;width:1200px;height:599px;background:linear-gradient(#2a2a2a,#1b1b1b)}
.services h2{color:var(--white)}
.services .title-rule{background:var(--white)}
.gallery{left:79px;top:146px;width:1042px;height:398px;display:flex}
.gallery div{flex:1;height:100%}
.g1{background:linear-gradient(#e7e1d8,#b89e7e)}
.g2{background:linear-gradient(#9fb0b9,#3f4c55)}
.g3{background:linear-gradient(#efece6,#a7866a)}
.g4{background:linear-gradient(#f1efec,#c9c2b8)}
.caption{left:79px;top:496px;width:261px;height:48px;background:var(--red);color:var(--white);font-size:17px;line-height:48px;padding-left:22px}

/* booking */
.booking{left:0;top:1830px;width:1200px}
.form{left:79px;top:1942px;width:666px}
.field{height:40px;border:1px solid var(--line);font-size:11px;color:#999;padding:12px 14px;margin-bottom:14px;position:relative}
.row{display:flex;gap:16px}
.row .field{flex:1}
.field svg{position:absolute;right:12px;top:16px}
.field.message{height:108px}
.submit{width:262px;height:40px;background:var(--ink);color:var(--white);font-size:16px;text-align:center;line-height:40px;margin-top:12px}
.maid-photo{left:826px;top:1880px;width:252px;height:491px;background:radial-gradient(ellipse at 50% 45%,#d9cbb8 0%,#eee8df 45%,#ffffff 75%)}

/* stats */
.stats{left:0;top:2443px;width:1200px;height:151px;background:var(--red);color:var(--white)}
.stat{top:40px;display:flex;align-items:center;gap:16px;font-weight:700;font-size:16px;line-height:20px}
.divider{top:0;height:151px}

/* testimonials */
.testimonials{left:0;top:2640px;width:1200px}
.quote{top:2730px;width:320px;height:125px;border:1px solid var(--line);padding:30px 24px 0 70px;font-style:italic;font-size:13px;line-height:22px;color:#888}
.quote.active{background:var(--light);border-color:var(--light)}
.quote .mark{position:absolute;left:20px;top:26px;font-family:Georgia,serif;font-size:52px;line-height:40px;color:#ccc;font-style:normal}
.quote.active .mark{color:var(--red)}
.person{top:2866px;width:120px;text-align:center;font-size:11px;color:#ccc}
.person .dot{width:8px;height:8px;border-radius:50%;background:#ccc;margin:0 auto}
.person .stem{width:2px;height:14px;background:#ccc;margin:0 auto 2px}
.person .avatar{width:60px;height:60px;border-radius:50%;border:2px solid #ccc;background:#e6e6e6;margin:0 auto 8px}
.person.active{color:var(--ink)}
.person.active .dot,.person.active .stem{background:var(--red)}
.person.active .avatar{border-color:var(--red);background:#c9c9c9}

/* partners */
.partners{left:0;top:3025px;width:1200px;height:153px;background:#f2f2f2;display:flex;justify-content:space-around;align-items:center;padding:0 60px}
.partner{font-size:26px;font-weight:500;color:#555}

/* footer */
.footer{left:0;top:3178px;width:1200px;height:319px;background:linear-gradient(#232323,#1b1b1b);color:var(--white);font-size:13px}
.footer h4{font-weight:400;font-size:14px;margin-bottom:28px}
.footer .about{left:79px;top:76px;width:260px;line-height:20px}
.footer .about .brand{position:static;margin-bottom:20px}
.footer .about .name{color:var(--white)}
.footer .links{left:432px;top:80px;line-height:17px}
.footer .contact{left:612px;top:80px}
.footer .contact dl{display:grid;grid-template-columns:88px 250px;row-gap:16px;line-height:18px}
.footer .follow{left:972px;top:80px}
.footer .icons{display:flex;gap:22px;margin-bottom:16px}
.footer .icons span{width:12px;height:12px;border-radius:50%;background:var(--white)}
.copyright{left:0;top:3500px;width:1200px;height:93px;background:var(--ink);color:#ccc;font-size:12px;border-top:1px solid #444}
.copyright span{position:absolute;top:38px}
</style>
</head>
<body>

<div class="abs topbar">
  <div class="abs social"><span></span><span></span><span></span><span></span></div>
  <div class="abs contact">
    <span><svg width="14" height="10" viewBox="0 0 14 10"><rect x="0.5" y="0.5" width="13" height="9" fill="none" stroke="#fff"/><path d="M1 1l6 5 6-5" fill="none" stroke="#fff"/></svg>hello@tidewellcleaning.com</span>
    <span><svg width="9" height="14" viewBox="0 0 9 14"><rect x="0.5" y="0.5" width="8" height="13" rx="1.5" fill="none" stroke="#fff"/><circle cx="4.5" cy="11" r="1" fill="#fff"/></svg>555-314-2760</span>
  </div>
</div>

<header class="abs header">
  <div class="abs brand"><div class="mark"></div><div class="name">Tidewell<br>Cleaning Services</div></div>
  <nav class="abs nav"><span>Home</span><span>About</span><span>Services &amp; pricing</span><span>FAQ</span><span>Login</span><span>Contact Us</span></nav>
  <div class="abs free-quote">FREE<br>QUOTE</div>
</header>

<section class="abs hero">
  <div class="photo" role="img" aria-label="Window cleaners in harnesses working on a glass office tower"></div>
  <svg class="curve" width="1200" height="40" viewBox="0 0 1200 40"><path d="M0 0Q600 60 1200 0V40H0Z" fill="#fff"/></svg>
  <h1 class="abs">Our Cleaning services</h1>
  <p class="abs">Seasonal Deep Cleaning, Window cleaning, Event Cleaning, Floor and Carpet Cleaning, Floor Striping and Waxing We cover Millbrook, Ashford, Easton Falls, Cedarvale, Harlow</p>
  <div class="abs btn">CONTACT US</div>
</section>

<section class="abs quality">
  <div class="title-rule"></div>
  <h2>Highest Quality Cleaning in affordable prices</h2>
  <p class="lead" style="margin-top:16px">Sed ut perspiciatis unde omnis iste natus error sit voluptatem accusantium doloremque laudantium, totam rem aperiam, eaque ipsa quae ab illo inventore veritatis et quasi architecto beatae vitae dicta sunt explicabo. Nemo enim ipsam voluptatem quia voluptas sit aspernatur aut odit aut fugit, sed quia consequuntur magni dolores eos qui ratione voluptatem sequi nesciunt.</p>
</section>
<div class="abs team-photo" role="img" aria-label="Cheerful cleaning team in blue aprons holding mops and sprays"></div>

<div class="abs feature" style="top:814px">
  <div class="icon"><svg width="30" height="30" viewBox="0 0 30 30"><rect x="9" y="3" width="12" height="24" rx="2" fill="none" stroke="#fff" stroke-width="2"/><circle cx="15" cy="23" r="1.5" fill="#fff"/></svg></div>
  <div><h3>Book Us</h3><p>Sed ut perspiciatis unde omnis iste natus error sit voluptatem nesciunt.</p></div>
</div>
<div class="abs feature" style="top:924px">
  <div class="icon"><svg width="30" height="30" viewBox="0 0 30 30"><path d="M8 26h14l-2-12H10z" fill="#fff"/><rect x="13" y="4" width="4" height="10" fill="#fff"/></svg></div>
  <div><h3>Clean</h3><p>Sed ut perspiciatis unde omnis iste natus error sit voluptatem nesciunt.</p></div>
</div>
<div class="abs feature" style="top:1034px">
  <div class="icon"><svg width="30" height="30" viewBox="0 0 30 30"><circle cx="15" cy="8" r="4" fill="#fff"/><path d="M5 24q10-14 20 0z" fill="#fff"/></svg></div>
  <div><h3>Relax</h3><p>Sed ut perspiciatis unde omnis iste natus error sit voluptatem nesciunt.</p></div>
</div>

<section class="abs services">
  <div class="title-rule" style="margin-top:48px;margin-bottom:0"></div>
  <h2 style="margin-top:10px">Service We Provide</h2>
  <div class="abs gallery">
    <div class="g1" role="img" aria-label="Cleaner mopping a wooden floor"></div>
    <div class="g2" role="img" aria-label="Window cleaner on a glass facade"></div>
    <div class="g3" role="img" aria-label="Cleaner vacuuming a living room"></div>
    <div class="g4" role="img" aria-label="Cleaner mopping near a wet floor sign"></div>
  </div>
  <div class="abs caption">Seasonal Deep Cleaning</div>
</section>

<section class="abs booking">
  <div class="title-rule"></div>
  <h2>Book cleaning service</h2>
</section>
<form class="abs form">
  <div class="field">Full Name</div>
  <div class="row"><div class="field">Full Name</div><div class="field">Phone Number</div></div>
  <div class="field">Address</div>
  <div class="row"><div class="field">City</div><div class="field">Zipcode</div></div>
  <div class="row">
    <div class="field">Choose a service<svg width="10" height="6" viewBox="0 0 10 6"><path d="M1 1l4 4 4-4" fill="none" stroke="#999"/></svg></div>
    <div class="field">Choose a Option<svg width="10" height="6" viewBox="0 0 10 6"><path d="M1 1l4 4 4-4" fill="none" stroke="#999"/></svg></div>
  </div>
  <div class="field message">Your Massage</div>
  <div class="submit">Submit</div>
</form>
<div class="abs maid-photo" role="img" aria-label="Smiling cleaner leaning on a mop beside a cleaning cart"></div>

<section class="abs stats">
  <div class="abs stat" style="left:112px">
    <svg width="62" height="74" viewBox="0 0 62 74"><circle cx="31" cy="28" r="24" fill="none" stroke="#fff" stroke-width="4"/><path d="M20 28l8 8 14-16" fill="none" stroke="#fff" stroke-width="4"/><path d="M18 50l-6 22 19-8 19 8-6-22" fill="none" stroke="#fff" stroke-width="3"/></svg>
    <div>950<br>Quality of staffs</div>
  </div>
  <svg class="abs divider" style="left:387px;width:40px" viewBox="0 0 40 151"><path d="M30 25L10 126" stroke="#fff" stroke-opacity=".6" stroke-width="2"/></svg>
  <div class="abs stat" style="left:462px">
    <svg width="80" height="70" viewBox="0 0 80 70"><circle cx="16" cy="12" r="7" fill="#fff"/><rect x="9" y="22" width="14" height="46" fill="#fff"/><circle cx="64" cy="8" r="7" fill="#fff"/><rect x="57" y="18" width="14" height="50" fill="#fff"/><path d="M23 30l34-6" stroke="#fff" stroke-width="4"/></svg>
    <div>365<br>Day Working</div>
  </div>
  <svg class="abs divider" style="left:746px;width:40px" viewBox="0 0 40 151"><path d="M30 25L10 126" stroke="#fff" stroke-opacity=".6" stroke-width="2"/></svg>
  <div class="abs stat" style="left:790px">
    <svg width="88" height="70" viewBox="0 0 88 70"><rect x="2" y="20" width="30" height="48" fill="none" stroke="#fff" stroke-width="4"/><rect x="38" y="2" width="48" height="66" fill="none" stroke="#fff" stroke-width="4"/><g fill="#fff"><rect x="46" y="12" width="8" height="8"/><rect x="58" y="12" width="8" height="8"/><rect x="70" y="12" width="8" height="8"/><rect x="46" y="28" width="8" height="8"/><rect x="58" y="28" width="8" height="8"/><rect x="70" y="28" width="8" height="8"/><rect x="46" y="44" width="8" height="8"/><rect x="70" y="44" width="8" height="8"/><rect x="10" y="30" width="6" height="6"/><rect x="18" y="30" width="6" height="6"/><rect x="10" y="44" width="6" height="6"/><rect x="18" y="44" width="6" height="6"/></g></svg>
    <div>1790<br>Clean Office Doors</div>
  </div>
</section>

<section class="abs testimonials">
  <div class="title-rule"></div>
  <h2>Some Impressions From Our Customers !</h2>
</section>
<div class="abs quote" style="left:79px"><span class="mark">“</span>Neque porro quisquam est, qui dolorem ipsum quia dolor sit amet, consectetur, adipisci velit, sed quia</div>
<div class="abs quote active" style="left:440px"><span class="mark">“</span>Neque porro quisquam est, qui dolorem ipsum quia dolor sit amet, consectetur, adipisci velit, sed quia</div>
<div class="abs quote" style="left:801px"><span class="mark">“</span>Neque porro quisquam est, qui dolorem ipsum quia dolor sit amet, consectetur, adipisci velit, sed quia</div>
<div class="abs person" style="left:179px"><div class="dot"></div><div class="stem"></div><div class="avatar"></div>DANA ORTIZ</div>
<div class="abs person active" style="left:540px"><div class="dot"></div><div class="stem"></div><div class="avatar"></div>DANA ORTIZ</div>
<div class="abs person" style="left:901px"><div class="dot"></div><div class="stem"></div><div class="avatar"></div>DANA ORTIZ</div>

<section class="abs partners">
  <div class="partner">Northfield Partners</div>
  <div class="partner">Larkspur Radio</div>
  <div class="partner">Merrow Network</div>
  <div class="partner">Quillon Group</div>
</section>

<footer class="abs footer">
  <div class="abs about">
    <div class="brand"><div class="mark"></div><div class="name">Tidewell<br>Cleaning Services</div></div>
    <p>Sed ut perspiciatis unde omnis iste natus error sit accusantium doloremque totam rem aperiam.</p>
  </div>
  <div class="abs links"><h4>QUICK LINK</h4>Home<br>About<br>Services &amp; pricing<br>FAQ<br>Login<br>Contact Us</div>
  <div class="abs contact"><h4>CONTACT US</h4>
    <dl><dt>Address</dt><dd>12 Orchard Row, Riverside,<br>NY 12001</dd><dt>Mobile No:</dt><dd>555-314-2760</dd><dt>Email:</dt><dd>hello@tidewellcleaning.com</dd></dl>
  </div>
  <div class="abs follow"><h4>FOLLOW US</h4>
    <div class="icons"><span></span><span></span><span></span><span></span></div>
    <div><svg width="16" height="14" viewBox="0 0 16 14" style="vertical-align:-2px;margin-right:10px"><path d="M1 1h14v9H6l-4 3V10H1z" fill="#fff"/></svg>Live Chat With Us</div>
  </div>
</footer>
<div class="abs copyright"><span style="left:96px">Copyright © 2017, all right reserved</span><span style="right:78px">Term &amp; Conditions</span></div>

</body>
</html>
```